Business Card Design Project for Architecture and Interior Design company

We need a business card design and logo for an architecture and design firm located in Santiago de Chile. It´s a small company, and the name is "Vostiq" ("Vost" from my surname Vostani, and "arq" for arquitectura or architecture. But it would also be nice that the logo comunicates de Word game "Vosta" as beautiful in italian, and "arq" as architecture".
The idea is to give a delicate, elegant and sofisticated, yet fresh image. Would prefer grey black and white colors, but wouldn´t mind to use another additional color.
I allready have a web page www.vostiq.cl, but would like to improve the logo design.
Please contact if any further information is requiered.
Reason: Need a more arquitectural and desing spirit in the cards. Few of them give that idea.

```html
<!DOCTYPE html>
<html lang="es">
<head>
<meta charset="utf-8">
<title>Vostiq — Tarjetas de presentación</title>
<link href="https://fonts.googleapis.com/css2?family=Open+Sans:wght@400&display=swap" rel="stylesheet">
<style>
  :root {
    --backdrop: #e9eaea;
    --paper: #ffffff;
    --ink: #5a5a5a;
    --ink-soft: #6b6b6b;
    --band: #5b5b5b;
    --reverse-ink: #ececec;
  }
  * { margin: 0; padding: 0; box-sizing: border-box; }
  html, body { width: 1200px; height: 900px; overflow: hidden; }
  body {
    background: var(--backdrop);
    font-family: "Open Sans", sans-serif;
    color: var(--ink);
    position: relative;
  }
  .card {
    position: absolute;
    background: var(--paper);
    box-shadow: 0 6px 18px rgba(0,0,0,0.12);
  }
  /* Horizontal card */
  .card--landscape {
    left: 60px; top: 150px; width: 500px; height: 290px;
  }
  .card--landscape .wordmark {
    position: absolute; left: 70px; top: 120px;
    font-size: 40px; line-height: 1;
  }
  .card--landscape .divider {
    position: absolute; left: 262px; top: 95px;
    width: 1px; height: 80px; background: var(--ink);
  }
  .card--landscape .contact {
    position: absolute; left: 278px; top: 100px;
    font-size: 11px; line-height: 1.35; color: var(--ink-soft);
  }
  .contact .name { font-size: 12px; }
  .contact .role { font-size: 9px; text-align: right; margin-bottom: 8px; }

  /* Vertical card */
  .card--portrait {
    left: 650px; top: 80px; width: 330px; height: 500px;
    overflow: hidden;
  }
  .card--portrait .name {
    position: absolute; left: 36px; top: 40px; font-size: 13px;
  }
  .card--portrait .wordmark {
    position: absolute; left: 0; right: 0; top: 190px;
    text-align: center; font-size: 44px; line-height: 1;
  }
  .card--portrait .role {
    position: absolute; left: 0; right: 0; top: 246px;
    text-align: center; font-size: 11px; letter-spacing: 3px; color: var(--ink-soft);
  }
  .card--portrait .contact {
    position: absolute; right: 36px; top: 332px;
    text-align: right; font-size: 13px; line-height: 1.35;
  }
  .card--portrait .band {
    position: absolute; left: 0; right: 0; bottom: 0; height: 70px;
    background: var(--band);
  }

  /* Logo variants */
  .logo-light {
    position: absolute; left: 118px; top: 752px;
    font-size: 92px; line-height: 1; color: var(--ink);
  }
  .logo-dark-panel {
    position: absolute; left: 592px; top: 722px; width: 585px; height: 162px;
    background: var(--band);
  }
  .logo-dark-panel .wordmark {
    position: absolute; left: 120px; top: 30px;
    font-size: 92px; line-height: 1; color: var(--reverse-ink);
  }
</style>
</head>
<body>
  <section class="card card--landscape">
    <div class="wordmark">Vostiq</div>
    <div class="divider"></div>
    <div class="contact">
      <div class="name">Anaya Vostani Ramdani</div>
      <div class="role">Arquitecto</div>
      <div>Mobile: +56 9 41528376</div>
      <div>e-mail: avostani@vostiq.cl</div>
      <div>Web: www.vostiq.cl</div>
    </div>
  </section>

  <section class="card card--portrait">
    <div class="name">Anaya Vostani Ramdani</div>
    <div class="wordmark">Vostiq</div>
    <div class="role">Arquitecto</div>
    <div class="contact">
      <div>Mobile: +56 9 41528376</div>
      <div>e-mail: avostani@vostiq.cl</div>
      <div>Web: www.vostiq.cl</div>
    </div>
    <div class="band"></div>
  </section>

  <div class="logo-light">Vostiq</div>
  <div class="logo-dark-panel"><div class="wordmark">Vostiq</div></div>
</body>
</html>
```